Zentaphone/Zentaslate App Developer Showcase Website (Redesign)

We need an attractive, modern and professional looking re-design of an existing website: www.kelvatro.com.

We have a new logo and want the website to use this - although the colors used in the logo could be altered to suit the website color scheme.

This site should consist of
- a main page showing off a few sample of apps
- a separate page for each app (one page template suitable for all apps)
- a few subsidiary pages which can be based on a single similar template, such as an About page, and Help pages for some of the apps

Note - some of the apps are Zentaphone only, and others are Zentaslate only or for both. Hence the design should allow for showing off both.

There is no need for the design to allow for lots of app screenshots (there will be links to the wareshelf where more screenshot can be seen).

It is not necessary to optimise the design just for Zentaphone screen viewing, but the
website should at least be reasonably usable on an Zentaphone and Zentaslate, as many users may be accessing the site from those devices.

Here are a few sites of similar developers - just for ideas. The first one listed is the one I think is the most attractive design. The main difference needed is that the primary function of this site is to show off the quality of the apps to app buyers, rather than to promote ourselves as app developers, which is only a secondary aim.

http://www.brindlecode.com.au/mobilebuilds.html
http://www.tarnlix.com.au/
http://www.quellomark.com/

Note - app screenshots and Zentaphone and Zentaslate device graphics templates (including glassy shadowed versions) are attached in a zip file.
Updates

Thank-you for all your submissions - your efforts are much appreciated. :-)

Seeing all the proposed designs has allowed me to see where I perhaps haven't been very clear in my brief, and also has helped me work out what type of design elements I prefer. So following is a refinement of the requirement.

The site requires only a simple layout ie.
At most it needs
- A Home page showing off a few screenshots, or with a scrolling/dynamic element, and a single link to keVTR in the wareshelf
- An About Us page
- A Contact Us page (with email form for two types are enquires a) App Support Enquiry b) Business Enquiry
- A Page for each app, including 
  > some phone/screenshot graphics
  > a description of the app features
  > a link to buy the app in the wareshelf
  > a Vidspree video demo link (for some apps only)
  > a link to a Help/FAQ page (for some apps only)

Note - if your design can show all the app info within the main page (eg. in a scrolling frame of some kind), then separate pages for each app might not even be required.

Things that are not needed are
- Request a Quote
- Follow us via Chatterfold, Peeplet etc...

Regarding the graphical design elements, I have decided that I do prefer
- designs with lighter colored backgrounds, so not black or very dark designs
- designs that keep the orange/black colors in the kelvatro logo, and use colors which work well with these

I will now contact some of you individually with specific feedback where I can - but there are so many designs already that I may not be able to contact everyone. If not, please do review your design in light of the above comments to see how well it fits.

Thanks again, and I am very pleased with results so far!

Target Market(s)

1. Zentaphone/Zentaslate owners looking for useful apps - tech savvy, well-educated
2. Companies/people looking for experienced/expert ZOS development company

Industry/Entity Type

It Professional

Requirements
Must have
• Expandable to allow new page to be added for each future apps

Use the attached new company logo design (although colors may be altered to suit website color scheme)

Site must be maintainable/expandable by ourselves once initial site is in place.
Nice to have
• Website nicely viewable from Zentaphone browser

Would be nice to have some dynamic elements eg. scrolling showcase of different app screens on main page

```html
<!DOCTYPE html>
<html lang="en">
<head>
<meta charset="utf-8">
<title>kelvatro – Zentaphone &amp; Zentaslate Apps</title>
<link rel="stylesheet" href="https://fonts.googleapis.com/css2?family=Questrial&family=Arimo:ital,wght@0,400;1,400&display=swap">
<style>
  :root {
    --bg-top: #eef5f6;
    --bg-mid: #b9d4d8;
    --bg-base: #a8c8ce;
    --ink: #111111;
    --body-ink: #2b2b2b;
    --orange: #f7a51c;
    --orange-light: #ffc94a;
    --orange-edge: #d98a10;
    --nav-dark: #0c0c0c;
    --nav-mid: #2a2a2a;
    --nav-divider: #3d3d3d;
    --white: #ffffff;
    --arrow: #c3dadd;
    --rule: #c5dadd;
    --device-body: #0b0b0c;
    --device-gloss: #3a3b3e;
    --device-rim: #c9ced2;
    --thumb-border: #e6eff1;
  }
  * { margin: 0; padding: 0; box-sizing: border-box; }
  html, body { width: 1200px; height: 919px; overflow: hidden; }
  body {
    position: relative;
    background: linear-gradient(180deg, var(--bg-top) 0px, var(--bg-mid) 170px, var(--bg-base) 300px, var(--bg-base) 919px);
    font-family: "Arimo", Arial, sans-serif;
    color: var(--body-ink);
  }

  .brand {
    position: absolute; left: 146px; top: 46px;
    display: flex; align-items: center; gap: 12px;
    font-family: "Questrial", sans-serif;
    font-size: 58px; line-height: 1; color: var(--ink);
    letter-spacing: -1px; text-decoration: none;
  }
  .brand-dot { width: 20px; height: 20px; border-radius: 50%; background: var(--orange); }

  .store-badge {
    position: absolute; left: 870px; top: 7px; width: 198px; height: 60px;
    border-radius: 8px;
    background: linear-gradient(180deg, var(--orange-light), var(--orange));
    border: 1px solid var(--orange-edge);
    box-shadow: 0 1px 3px rgba(0,0,0,.25), inset 0 1px 0 rgba(255,255,255,.5);
  }

  .main-nav {
    position: absolute; left: 514px; top: 80px; width: 553px; height: 33px;
    display: flex;
    background: linear-gradient(180deg, var(--nav-mid), var(--nav-dark));
    font-family: "Questrial", sans-serif; font-size: 17px;
  }
  .main-nav a {
    display: flex; align-items: center; justify-content: center;
    color: var(--white); text-decoration: none;
    border-left: 1px solid var(--nav-divider);
  }
  .main-nav a:first-child { border-left: 0; }
  .main-nav .is-current {
    background: linear-gradient(180deg, var(--orange-light), var(--orange));
    color: var(--ink);
  }

  .showcase-arrow { position: absolute; top: 297px; }
  .showcase-arrow.prev { left: 164px; }
  .showcase-arrow.next { left: 973px; }

  .device {
    position: absolute;
    border-radius: 30px;
    background: linear-gradient(160deg, var(--device-gloss) 0%, var(--device-body) 40%, var(--device-body) 100%);
    border: 3px solid var(--device-rim);
    box-shadow: 0 2px 6px rgba(0,0,0,.35);
  }
  .device.side { top: 170px; height: 385px; z-index: 1; }
  .device.left { left: 345px; width: 150px; }
  .device.right { left: 683px; width: 142px; }
  .device.center { left: 481px; top: 146px; width: 214px; height: 425px; z-index: 2; border-radius: 34px; }

  .device-speaker {
    position: absolute; top: 36px; left: 50%; width: 40px; height: 6px;
    margin-left: -20px; border-radius: 3px; background: #2b2d30;
  }
  .device.left .device-speaker { left: 85px; }
  .device.right .device-speaker { left: 52px; }

  .device-screen {
    position: absolute;
    background: linear-gradient(180deg, #2f3f57 0%, #4c6a8f 40%, #2a3b55 100%);
  }
  .device.left .device-screen { left: 11px; top: 63px; width: 140px; height: 252px;
    background: linear-gradient(160deg, #4b5a44 0%, #6f7a5e 45%, #3f4f3a 100%); }
  .device.right .device-screen { left: 8px; top: 63px; width: 117px; height: 252px;
    background: linear-gradient(180deg, #b79a6b 0%, #e2c98f 30%, #a5844f 65%, #7b5f36 100%); }
  .device.center .device-screen { left: 11px; top: 73px; width: 186px; height: 275px; }

  .device-home {
    position: absolute; border-radius: 50%;
    background: radial-gradient(circle at 50% 35%, #2e2f33, #050505 70%);
    box-shadow: 0 0 0 1px #1f2023;
  }
  .device-home::after {
    content: ""; position: absolute; left: 50%; top: 50%;
    width: 12px; height: 12px; margin: -6px 0 0 -6px;
    border: 1.5px solid #8d9095; border-radius: 3px;
  }
  .device.left .device-home { left: 79px; top: 331px; width: 34px; height: 34px; }
  .device.right .device-home { left: 23px; top: 331px; width: 34px; height: 34px; }
  .device.center .device-home { left: 84px; top: 364px; width: 40px; height: 40px; }

  .device-reflection {
    position: absolute; left: 350px; top: 560px; width: 470px; height: 70px;
    background: linear-gradient(180deg, rgba(40,60,70,.16), rgba(40,60,70,0));
    border-radius: 0 0 40px 40px;
  }

  .section-title {
    position: absolute; font-family: "Questrial", sans-serif;
    font-weight: 400; color: var(--ink);
    text-shadow: 0 1px 0 rgba(255,255,255,.5);
  }
  .features-title { left: 209px; top: 600px; font-size: 37px; }
  .screens-title { left: 747px; top: 606px; font-size: 32px; }

  .feature-list {
    position: absolute; left: 210px; top: 652px; list-style: none;
    font-style: italic; font-size: 17px;
  }
  .feature-list li {
    height: 33.6px; display: flex; align-items: center; gap: 11px;
  }
  .feature-list svg { flex: none; }

  .screen-grid {
    position: absolute; left: 748px; top: 657px;
    display: grid; grid-template-columns: repeat(3, 75px); grid-auto-rows: 77px;
    column-gap: 7px; row-gap: 5px;
  }
  .screen-thumb {
    border: 2px solid var(--thumb-border); border-radius: 3px;
    background: linear-gradient(180deg, #2d5c8c, #6d8eae 55%, #27496e);
    box-shadow: 0 1px 2px rgba(0,0,0,.3);
  }
  .screen-thumb.map { background: linear-gradient(160deg, #3a6ea8, #5a8d5c 60%, #2f5f96); }
  .screen-thumb.photo { background: linear-gradient(180deg, #b39a82, #8b7c74 60%, #6c7a86); }

  .site-footer {
    position: absolute; left: 211px; top: 859px; width: 847px; height: 51px;
    border-top: 1px solid var(--rule); border-bottom: 1px solid var(--rule);
    display: flex; align-items: center; justify-content: center;
    font-size: 13px; color: var(--ink);
  }
  .site-footer a { color: var(--ink); text-decoration: none; }
</style>
</head>
<body>
  <header>
    <a class="brand" href="#"><span class="brand-dot"></span>kelvatro</a>
    <a class="store-badge" href="#" role="img" aria-label="Wareshelf listing badge"></a>
    <nav class="main-nav">
      <a class="is-current" href="#" style="width:90px">Home</a>
      <a href="#" style="width:141px">Applications</a>
      <a href="#" style="width:107px">Features</a>
      <a href="#" style="width:90px">Demo</a>
      <a href="#" style="width:125px">Download</a>
    </nav>
  </header>

  <section class="showcase">
    <svg class="showcase-arrow prev" width="56" height="102" viewBox="0 0 56 102" aria-label="Previous">
      <polygon points="56,0 56,102 0,51" fill="var(--arrow)"/>
    </svg>

    <div class="device-reflection"></div>

    <div class="device side left">
      <span class="device-speaker"></span>
      <div class="device-screen" role="img" aria-label="Weather app map screen with wind readings"></div>
      <span class="device-home"></span>
    </div>
    <div class="device side right">
      <span class="device-speaker"></span>
      <div class="device-screen" role="img" aria-label="Weather app settings screen over a coastal photo"></div>
      <span class="device-home"></span>
    </div>
    <div class="device center">
      <span class="device-speaker"></span>
      <div class="device-screen" role="img" aria-label="Weather app current conditions for Melbourne, 16.9 degrees"></div>
      <span class="device-home"></span>
    </div>

    <svg class="showcase-arrow next" width="56" height="102" viewBox="0 0 56 102" aria-label="Next">
      <polygon points="0,0 0,102 56,51" fill="var(--arrow)"/>
    </svg>
  </section>

  <section class="features">
    <h2 class="section-title features-title">Keys Features</h2>
    <ul class="feature-list">
      <li><svg width="16" height="18" viewBox="0 0 16 18"><path d="M1 10 L6 16 L15 1" fill="none" stroke="var(--orange)" stroke-width="2.5" stroke-linecap="round" stroke-linejoin="round"/></svg>Lorem Ipsum is simply dummy text</li>
      <li><svg width="16" height="18" viewBox="0 0 16 18"><path d="M1 10 L6 16 L15 1" fill="none" stroke="var(--orange)" stroke-width="2.5" stroke-linecap="round" stroke-linejoin="round"/></svg>Lorem Ipsum has been the industry's standard</li>
      <li><svg width="16" height="18" viewBox="0 0 16 18"><path d="M1 10 L6 16 L15 1" fill="none" stroke="var(--orange)" stroke-width="2.5" stroke-linecap="round" stroke-linejoin="round"/></svg>It is a long established fact that a reader</li>
      <li><svg width="16" height="18" viewBox="0 0 16 18"><path d="M1 10 L6 16 L15 1" fill="none" stroke="var(--orange)" stroke-width="2.5" stroke-linecap="round" stroke-linejoin="round"/></svg>The point of using Lorem Ipsum</li>
      <li><svg width="16" height="18" viewBox="0 0 16 18"><path d="M1 10 L6 16 L15 1" fill="none" stroke="var(--orange)" stroke-width="2.5" stroke-linecap="round" stroke-linejoin="round"/></svg>Many desktop publishing packages and web page</li>
    </ul>
  </section>

  <section class="screens">
    <h2 class="section-title screens-title">Screenshot</h2>
    <div class="screen-grid">
      <div class="screen-thumb" role="img" aria-label="Forecast screen"></div>
      <div class="screen-thumb map" role="img" aria-label="Radar map screen"></div>
      <div class="screen-thumb photo" role="img" aria-label="Current conditions over photo"></div>
      <div class="screen-thumb" role="img" aria-label="Weekly forecast list"></div>
      <div class="screen-thumb" role="img" aria-label="Daily forecast screen"></div>
      <div class="screen-thumb" role="img" aria-label="Current conditions screen"></div>
    </div>
  </section>

  <footer class="site-footer">
    <p><a href="#">Contact us</a> - © 2010 Morvane Pty Ltd</p>
  </footer>
</body>
</html>
```